Postcard Design

I need a postcard printed in black and white on one side only, with the name, address and a small logo in the shape of a beehive written straight along the top on one side.

I have a photo which I can send you of the logo

The wording is as follows......

Rosa Minter, The Larkspur, 52 Orchard Row, London NW6 4QT.
T: 020 7461 3820 M: 07924581307 E: rosa@rosaminterhome.example
www.rosaminterhome.example.

I would like the little beehive logo to go in the centre of the top line

Assuming the design is fine - it is not very difficult, please print 200 cards.

Target Market(s)

This is for private and business use

Font styles to use
Serif

Requirements
Must have
• Please choose a very classic font like book antica or Times new Roman. Can you choose a crisp and good quality white matt card for this.

```html
<!DOCTYPE html>
<html lang="en">
<head>
<meta charset="utf-8">
<title>Rosa Minter – Postcard</title>
<link rel="stylesheet" href="https://fonts.googleapis.com/css2?family=Sorts+Mill+Goudy&display=swap">
<style>
  :root {
    --backdrop: #ecebe7;
    --card: #ffffff;
    --ink: #111111;
    --emblem-light: #d9d9d6;
    --emblem-mid: #8c8c88;
    --emblem-dark: #3d3d3a;
  }
  * { box-sizing: border-box; margin: 0; padding: 0; }
  html, body {
    width: 1200px;
    height: 900px;
    overflow: hidden;
    background: var(--backdrop);
  }
  .canvas {
    width: 1200px;
    height: 900px;
    display: flex;
    align-items: center;
    justify-content: center;
  }
  .postcard {
    width: 900px;
    height: 680px;
    background: var(--card);
    box-shadow: 0 2px 10px rgba(0, 0, 0, 0.12);
    display: flex;
    flex-direction: column;
    align-items: center;
    padding-top: 44px;
  }
  .hive-emblem {
    display: block;
    width: 200px;
    height: 176px;
  }
  .sender-details {
    margin-top: 22px;
    font-family: "Sorts Mill Goudy", "Times New Roman", serif;
    font-size: 19px;
    line-height: 1.12;
    color: var(--ink);
    text-align: center;
    font-style: normal;
  }
  .sender-details .gap { display: inline-block; width: 0.55em; }
</style>
</head>
<body>
  <main class="canvas">
    <article class="postcard">
      <svg class="hive-emblem" viewBox="0 0 200 176" role="img" aria-label="Engraved illustration of a straw beehive on a wooden stand among leafy plants, with bees flying above">
        <defs>
          <radialGradient id="emblemTone" cx="50%" cy="58%" r="60%">
            <stop offset="0%" stop-color="var(--emblem-dark)"/>
            <stop offset="55%" stop-color="var(--emblem-mid)"/>
            <stop offset="100%" stop-color="var(--emblem-light)"/>
          </radialGradient>
        </defs>
        <rect width="200" height="176" fill="url(#emblemTone)"/>
      </svg>
      <address class="sender-details">
        <div>Rosa Minter, The Larkspur, 52 Orchard Row, London NW6 4QT.</div>
        <div>T: 020 7461 3820<span class="gap"></span>M: 07924581307<span class="gap"></span>E: rosa@rosaminterhome.example</div>
        <div>www.rosaminterhome.example.</div>
      </address>
    </article>
  </main>
</body>
</html>
```